Postcard double sided

Title: DWIGHT'S REVENGE

Why would Dwight Kessler align himself with Gordon Pruett?

(photo of two guys)

Dwight approached elected officials that he wanted to run for office, but did not have money to finance his campaign. He wanted other elected officials to finance his campaign. Everyone told him that they would help him get the vote out, but that he needed to finance his own race.

In comes Gordon Pruett.

Gordon Pruett who has a pay to play scheme over at the City, told Dwight he would finance his campaign on one condition.

He needed to run against Steven Hulse.

Why would Dwight want to run with no money?

Backside

DWIGHT'S REVENGE

Dwight decided to run because no one on the school board would terminate Dwight's ex and her new boyfriend who both work for the school district. His ex even filed criminal charges against him that are still pending.

Mug Shot facing left (name the charges Criminal Trespass , and Criminal Mischief (highlight bold letters use two lines) mug shot facing right

Complaint one (then photo with full face) Compliant 2)
(showcharges)

Dwight's ultimate goal is to terminate his ex and her new boyfriend if elected.
Plus Gordon Pruett needs the majority on the school board to do what he does bet.

Kickbacks for Contracts.

They will hire their own contractors!
Say "No" to Dwight's Revenge and Gordon Pruett Money Grab!

Title On Back: all caps: DOMESTIC VIOLENCE

```html
<!DOCTYPE html>
<html lang="en">
<head>
<meta charset="utf-8">
<title>Dwight's Revenge — Postcard</title>
<link rel="stylesheet" href="https://fonts.googleapis.com/css2?family=Black+Ops+One&family=Oswald:wght@600;700&family=Arimo:ital,wght@0,400;0,700;1,700&family=Share+Tech+Mono&display=swap">
<style>
  :root{
    --red:#c8101f;
    --red-dark:#9e0a16;
    --blue:#1e4f8f;
    --navy:#0f1f3d;
    --white:#ffffff;
    --paper:#f2f2f2;
    --ink:#222;
    --photo-a:#2c3f63;
    --photo-b:#7d8796;
    --mug-a:#8b8f93;
    --mug-b:#55595d;
  }
  *{box-sizing:border-box;margin:0;padding:0}
  html,body{width:1200px;height:1000px;overflow:hidden}
  body{background:var(--paper);position:relative;font-family:"Arimo",Arial,sans-serif}

  .card{position:absolute;background:var(--white);overflow:hidden}
  .card--front{left:267px;top:23px;width:692px;height:445px}
  .card--back{left:267px;top:516px;width:692px;height:446px}
  .abs{position:absolute}

  /* front */
  .front-header{left:0;top:0;width:692px;height:94px;background:linear-gradient(var(--red),var(--red-dark));text-align:center}
  .front-title{font-family:"Black Ops One",Impact,sans-serif;color:var(--white);font-size:38px;letter-spacing:1px;margin-top:15px;line-height:1;text-shadow:2px 2px 0 var(--navy)}
  .front-subtitle{color:var(--white);font-weight:700;font-size:17.5px;margin-top:6px}
  .front-band{left:0;top:94px;width:692px;height:208px;background:var(--blue)}
  .duo-photo{left:0;top:94px;width:378px;height:208px;background:linear-gradient(135deg,var(--photo-a),var(--photo-b))}
  .story{left:402px;top:110px;width:266px;color:var(--white);font-size:14.6px;line-height:1.3;text-align:justify}
  .story-kicker{margin-top:13px;font-weight:700;font-size:14.6px;text-align:left}
  .condition-pill{left:73px;top:277px;width:557px;height:70px;background:var(--red);border-radius:14px;color:var(--white);font-weight:700;font-size:17.5px;line-height:1.3;padding:11px 18px;text-align:center}
  .condition-pill em{font-style:italic}
  .condition-pill .hit{color:var(--navy);font-family:"Oswald",sans-serif;font-size:19px}
  .opponent-line{left:0;top:355px;width:692px;text-align:center;font-family:"Oswald",sans-serif;font-weight:700;color:var(--navy);font-size:25px;letter-spacing:.3px}
  .front-bar{left:0;top:399px;width:692px;height:38px;background:var(--navy);color:var(--white);font-weight:700;font-size:13.5px;text-align:center;line-height:38px}
  .red-strip{left:0;width:692px;height:8px;background:var(--red)}

  /* back */
  .back-design{left:0;top:0;width:447px;height:446px;overflow:hidden}
  .back-header{left:0;top:0;width:447px;height:47px;background:linear-gradient(var(--red),var(--red-dark));text-align:center}
  .back-title{font-family:"Black Ops One",Impact,sans-serif;color:var(--white);font-size:26px;line-height:50px;letter-spacing:1px;text-shadow:2px 2px 0 var(--navy)}
  .charges-band{left:0;top:47px;width:447px;height:115px;background:var(--navy)}
  .mug{width:72px;height:76px;background:linear-gradient(var(--mug-a),var(--mug-b))}
  .charge-label{width:90px;text-align:center;font-family:"Share Tech Mono",monospace;color:var(--white);font-size:10.5px;line-height:1.05;letter-spacing:.5px}
  .reason{left:107px;top:47px;width:232px;height:115px;background:var(--blue);color:var(--white);font-size:12.4px;line-height:1.3;text-align:center;padding:10px 10px}
  .complaint{width:166px;height:150px;background:var(--white);font-family:"Arimo",sans-serif;font-size:3.6px;line-height:1.35;color:var(--ink);padding:6px 6px;overflow:hidden}
  .complaint-head{display:flex;justify-content:space-between;font-weight:700}
  .complaint p{margin-top:3px}
  .sign-line{border-bottom:.5px solid var(--ink);width:56px;margin:4px 0 0 auto;height:10px}
  .face-photo{left:183px;top:162px;width:102px;height:150px;background:linear-gradient(var(--mug-a),var(--mug-b))}
  .goal-pill{left:31px;top:314px;width:388px;height:42px;background:var(--red);border-radius:10px;text-align:center;padding-top:7px;font-family:"Oswald",sans-serif;font-weight:600;font-size:10.5px;line-height:1.35}
  .goal-pill .goal-a{color:var(--navy);text-transform:uppercase}
  .goal-pill .goal-b{color:var(--white)}
  .kickbacks{left:0;top:363px;width:447px;text-align:center;font-family:"Oswald",sans-serif;font-weight:700;color:var(--navy);font-size:21px}
  .back-bar{left:0;top:396px;width:447px;height:43px;background:var(--navy);color:var(--white);font-family:"Oswald",sans-serif;font-weight:600;font-size:12.5px;line-height:1.3;text-align:center;padding-top:5px}

  /* mailing side */
  .mail-side{left:447px;top:0;width:245px;height:446px;background:var(--white)}
  .stamp-box{left:132px;top:29px;width:86px;height:86px;border:1px solid var(--ink)}
  .address-line{left:27px;width:191px;height:1px;background:#555}
</style>
</head>
<body>

<section class="card card--front" aria-label="Postcard front">
  <header class="abs front-header">
    <h1 class="front-title">DWIGHT'S REVENGE</h1>
    <p class="front-subtitle">Why would Dwight Kessler align himself with Gordon Pruett?</p>
  </header>
  <div class="abs front-band"></div>
  <div class="abs duo-photo" role="img" aria-label="Photo of Dwight Kessler and Gordon Pruett smiling in suits at a campaign backdrop"></div>
  <div class="abs story">
    <p>Dwight approached elected officials that he wanted to run for office, but did not have money to finance his campaign. He wanted other elected officials to finance his campaign. Everyone told him that they would help him get the vote out, but that he needed to finance his own race.</p>
    <p class="story-kicker">IN COMES GORDON PRUETT.</p>
  </div>
  <div class="abs condition-pill">Gordon Pruett who has a <em>pay to play scheme</em> over at the City, told Dwight he would finance his campaign <span class="hit">ON ONE CONDITION.</span></div>
  <p class="abs opponent-line">HE NEEDED TO RUN AGAINST STEVEN HULSE.</p>
  <p class="abs front-bar">WHY WOULD DWIGHT WANT TO RUN WITH NO MONEY?</p>
  <div class="abs red-strip" style="top:437px"></div>
</section>

<section class="card card--back" aria-label="Postcard back">
  <div class="abs back-design">
    <header class="abs back-header"><h2 class="back-title">DOMESTIC VIOLENCE</h2></header>
    <div class="abs charges-band"></div>
    <div class="abs mug" style="left:16px;top:58px" role="img" aria-label="Mug shot in profile facing left"></div>
    <p class="abs charge-label" style="left:7px;top:138px">CRIMINAL<br>TRESPASS</p>
    <div class="abs reason">Dwight decided to run because no one on the school board would terminate Dwight's ex and her new boyfriend who both work for the school district. His ex even filed criminal charges against him that are still pending.</div>
    <div class="abs mug" style="left:355px;top:58px" role="img" aria-label="Mug shot in profile facing right"></div>
    <p class="abs charge-label" style="left:346px;top:138px">CRIMINAL<br>MISCHIEF</p>

    <article class="abs complaint" style="left:10px;top:162px" aria-label="Complaint one">
      <div class="complaint-head"><span>THE STATE OF TEXAS<br>COUNTY OF HARLAN</span><span>CR-19-0000-F</span></div>
      <p>Before me, the undersigned, personally appeared the complainant who on oath states the accused did knowingly enter property of another.</p>
      <p>AGAINST THE PEACE AND DIGNITY OF THE STATE.</p>
      <div class="sign-line"></div>
      <p>In the name and by authority of the State of Texas, comes now the county attorney.</p>
      <p>AGAINST THE PEACE AND DIGNITY OF THE STATE.</p>
    </article>
    <div class="abs face-photo" role="img" aria-label="Front-facing mug shot of Dwight Kessler"></div>
    <article class="abs complaint" style="left:289px;top:162px;width:152px" aria-label="Complaint two">
      <div class="complaint-head"><span>THE STATE OF TEXAS<br>COUNTY OF HARLAN</span><span>CR-19-0001-F</span></div>
      <p>Before me, the undersigned, personally appeared the complainant who on oath states the accused did knowingly damage property of another.</p>
      <p>AGAINST THE PEACE AND DIGNITY OF THE STATE.</p>
      <div class="sign-line"></div>
      <p>In the name and by authority of the State of Texas, comes now the county attorney.</p>
      <p>AGAINST THE PEACE AND DIGNITY OF THE STATE.</p>
    </article>

    <div class="abs goal-pill">
      <p class="goal-a">Dwight's ultimate goal is to terminate his ex and her new boyfriend if elected.</p>
      <p class="goal-b">Plus Gordon Pruett needs the majority on the school board to do what he does bet.</p>
    </div>
    <p class="abs kickbacks">KICKBACKS FOR CONTRACTS.</p>
    <div class="abs back-bar">
      <p>THEY WILL HIRE THEIR OWN CONTRACTORS!</p>
      <p>SAY "NO" TO DWIGHT'S REVENGE AND GORDON PRUETT MONEY GRAB!</p>
    </div>
    <div class="abs red-strip" style="top:439px;width:447px"></div>
  </div>

  <div class="abs mail-side" aria-label="Mailing side">
    <div class="abs stamp-box"></div>
    <div class="abs address-line" style="top:196px"></div>
    <div class="abs address-line" style="top:226px"></div>
    <div class="abs address-line" style="top:256px"></div>
  </div>
</section>

</body>
</html>
```